Dunmore IT Services needs to look professional and modern

This is my first time using this site so I am unsure what to expect, I am very serious in needing design work done and have no issues paying for it. I am hoping for good things as my business needs this before I can make any money !
Dunmore IT Services Pty Ltd core business is small / medium business networking, support and related hardware ie servers, PC's, Laptops, network equipment/infrastructure, printers etc
The focus of the business to give our customers a competitive edge over others by using new and innovative technologies and services. This is always balanced against stability, reliability and efficiency of the customers IT network.
We are looking for the design of a logo and business cards (there is also the potential for a website once this project is successfully completed). The design should have a sense of refinement and stability while being modern. The choice of colour pallet is up to the designer but nothing gordy.
The cards need to be double sided with the reverse to include brief points of business offered, details of points to be filled in by me later.
The front needs to include business name, mobile number (0471 392 508), my name (Rob Dunmore), email address (rob@DunmoreITServices.com.au), website address (www.DunmoreITServices.com.au), business slogan ("Your Competitive Edge")
Business
"Your Competitive Edge"
Designer to choose colors to be used in the design.

```html
<!DOCTYPE html>
<html lang="en">
<head>
<meta charset="utf-8">
<title>Dunmore IT Services – Business Card</title>
<link rel="stylesheet" href="https://fonts.googleapis.com/css2?family=PT+Sans:wght@400;700&family=Open+Sans:ital,wght@1,700&display=swap">
<style>
  :root {
    --page-bg: #ffffff;
    --blue-deep: #1786bd;
    --blue-mid: #2198d0;
    --blue-light: #34ade3;
    --swoosh: rgba(255, 255, 255, 0.10);
    --text-light: #ffffff;
    --text-soft: #e8f5fc;
    --quote-grey: #3f4347;
    --mark-fill: #c9d8e2;
    --mark-faint: #eef2f5;
    --card-shadow: rgba(0, 0, 0, 0.28);
  }
  * { margin: 0; padding: 0; box-sizing: border-box; }
  html, body {
    width: 1200px;
    height: 1009px;
    overflow: hidden;
    background: var(--page-bg);
  }
  .sheet {
    position: relative;
    width: 1200px;
    height: 1009px;
  }
  .card {
    position: absolute;
    overflow: hidden;
    box-shadow: -4px 6px 14px var(--card-shadow);
  }
  .card--front {
    left: 268px;
    top: 60px;
    width: 683px;
    height: 393px;
    background: linear-gradient(180deg, var(--blue-deep) 0%, var(--blue-mid) 60%, var(--blue-light) 100%);
    font-family: "PT Sans", sans-serif;
    color: var(--text-light);
  }
  .card__swooshes {
    position: absolute;
    inset: 0;
  }
  .brand-block {
    position: absolute;
    left: 47px;
    top: 106px;
    width: 320px;
    text-align: center;
  }
  .brand-name {
    font-size: 26px;
    font-weight: 700;
    line-height: 32px;
  }
  .person {
    font-size: 22px;
    line-height: 30px;
  }
  .tagline {
    font-size: 18px;
    line-height: 24px;
    color: var(--text-soft);
  }
  .brand-mark {
    position: absolute;
    left: 363px;
    top: 55px;
    width: 236px;
    height: 236px;
    border-radius: 50%;
    background: var(--mark-fill);
  }
  .contact {
    position: absolute;
    left: 0;
    right: 0;
    top: 322px;
    text-align: center;
    font-size: 18px;
    line-height: 26px;
    color: var(--text-soft);
  }
  .card--back {
    left: 270px;
    top: 507px;
    width: 676px;
    height: 389px;
    background: var(--page-bg);
  }
  .back-mark {
    position: absolute;
    left: 329px;
    top: 5px;
    width: 368px;
    height: 368px;
    border-radius: 50%;
    background: var(--mark-faint);
  }
  .mission {
    position: absolute;
    left: 126px;
    top: 122px;
    font-family: "Open Sans", sans-serif;
    font-style: italic;
    font-weight: 700;
    font-size: 19px;
    line-height: 27px;
    color: var(--quote-grey);
    white-space: pre;
  }
</style>
</head>
<body>
  <main class="sheet">
    <section class="card card--front">
      <svg class="card__swooshes" width="683" height="393" viewBox="0 0 683 393" aria-hidden="true">
        <path d="M0 260 C 200 180, 420 200, 683 120 L683 393 L0 393 Z" fill="var(--swoosh)"/>
        <path d="M60 0 C 160 120, 380 210, 683 230 L683 260 C 380 250, 140 160, 30 0 Z" fill="var(--swoosh)"/>
        <path d="M0 340 C 250 300, 480 330, 683 300 L683 393 L0 393 Z" fill="var(--swoosh)"/>
      </svg>
      <div class="brand-block">
        <div class="brand-name">Dunmore IT Services</div>
        <div class="person">Rob Dunmore | Co-Founder</div>
        <div class="tagline">Your Competitive Edge</div>
      </div>
      <div class="brand-mark" aria-hidden="true"></div>
      <div class="contact">
        <div>email:rob@DunmoreITServices.com.au</div>
        <div>P: 0471 392 508 | www.DunmoreITServices.com.au</div>
      </div>
    </section>

    <section class="card card--back">
      <div class="back-mark" aria-hidden="true"></div>
      <p class="mission">“The focus of the business to give our
 customers a competitive edge
 over others by using new and innovative
technologies and services”</p>
    </section>
  </main>
</body>
</html>
```